Pellham Ridge Nectar Company, local Honey producer needs product Lable to encourage sales

We are a small business (Pellham Ridge Nectar Company) located in a small Texas town that harvests honey from our beehives yearly. Our honey would be considered "raw wildflower honey" and our goal is to sell it locally (farmers markets) and to surrounding areas.

We are currently packaging in plastic classic honey bottles with white flip caps. Sizes are 8oz and 16oz bottles (see pictures for actual size). Larger orders will be filled in one quart mason jars.

Design Ideas:
-vintage style design with bee or several bees in background
- incorporate company name "Pellham Ridge Nectar Company"
- needs small description "Raw Honey", and "Harvested in Marlow Creek, Idaho"

Target Market(s)

Farmers markets, health conscience people looking for unprocessed food options

Industry/Entity Type

Small Business

Requirements
Nice to have
• Vintage feel
Should not have
• No cartoonish characters

```html
<!DOCTYPE html>
<html lang="en">
<head>
<meta charset="utf-8">
<title>Pellham Ridge Nectar Company – Raw Honey Label</title>
<link rel="stylesheet" href="https://fonts.googleapis.com/css2?family=Lobster&family=Josefin+Sans:wght@400;600&display=swap">
<style>
  :root {
    --backdrop: #ece6da;
    --label-rim: #3a1a0e;
    --label-core: #a3222a;
    --label-mid: #7d1a1c;
    --label-edge: #4a1410;
    --honey-yellow: #f7cf2f;
    --comb-gold: #f0c419;
    --comb-light: #fff3c4;
    --cream: #fff7e6;
  }
  html, body {
    margin: 0;
    width: 1200px;
    height: 1000px;
    overflow: hidden;
    background: var(--backdrop);
  }
  .canvas {
    width: 1200px;
    height: 1000px;
    display: flex;
    align-items: center;
    justify-content: center;
  }
  .label {
    width: 500px;
    height: 860px;
    border-radius: 250px;
    background: var(--label-rim);
    padding: 14px;
    box-sizing: border-box;
  }
  .label-face {
    width: 100%;
    height: 100%;
    border-radius: 236px;
    border: 4px solid var(--cream);
    box-sizing: border-box;
    background: radial-gradient(ellipse at 50% 48%, var(--label-core) 0%, var(--label-mid) 55%, var(--label-edge) 100%);
    display: flex;
    flex-direction: column;
    align-items: center;
    justify-content: center;
    padding: 40px 30px;
    text-align: center;
  }
  .brand-dot {
    width: 18px;
    height: 18px;
    border-radius: 50%;
    background: var(--honey-yellow);
    margin-bottom: 16px;
  }
  .brand-name {
    margin: 0;
    font-family: "Lobster", cursive;
    font-weight: 400;
    color: var(--honey-yellow);
    display: flex;
    flex-direction: column;
    align-items: center;
    font-size: 62px;
    line-height: 1.05;
  }
  .brand-name .brand-key {
    font-size: 112px;
    line-height: 1.05;
  }
  .honeycomb {
    width: 180px;
    height: 92px;
    margin-top: 36px;
    border-radius: 10px;
    background: linear-gradient(135deg, var(--comb-gold), var(--comb-light) 55%, var(--comb-gold));
  }
  .product-type {
    margin: 34px 0 0;
    font-family: "Josefin Sans", sans-serif;
    font-weight: 600;
    font-size: 40px;
    line-height: 1.1;
    color: var(--honey-yellow);
  }
  .origin {
    margin: 14px 0 0;
    font-family: "Josefin Sans", sans-serif;
    font-weight: 400;
    font-size: 20px;
    line-height: 1.2;
    color: var(--cream);
  }
  .net-weight {
    margin: 28px 0 0;
    font-family: "Josefin Sans", sans-serif;
    font-weight: 400;
    font-size: 26px;
    line-height: 1.2;
    color: var(--honey-yellow);
  }
</style>
</head>
<body>
  <main class="canvas">
    <article class="label">
      <div class="label-face">
        <span class="brand-dot"></span>
        <h1 class="brand-name">
          <span>Pellham Ridge</span>
          <span class="brand-key">Nectar</span>
          <span>Company</span>
        </h1>
        <div class="honeycomb" role="img" aria-label="Cluster of yellow and white honeycomb cells"></div>
        <p class="product-type">Raw Honey</p>
        <p class="origin">Harvested in Marlow Creek, Idaho</p>
        <p class="net-weight">8oz. (226G)</p>
      </div>
    </article>
  </main>
</body>
</html>
```